Letterhead

We would like to use the logo attached as a new letterhead. Our problem is that we think the dark blue background is too much. We'd like a sleek, professional letterhead, and we'd like at least five options to choose from. I've also uploaded our old letterhead for reference of the style we're going for.

```html
<!DOCTYPE html>
<html lang="en">
<head>
<meta charset="utf-8">
<title>Kestrel Bay Strategies Letterhead</title>
<link href="https://fonts.googleapis.com/css2?family=Tinos:wght@400;700&family=Cinzel:wght@500&display=swap" rel="stylesheet">
<style>
  :root {
    --navy: #1c2e4a;
    --gold-deep: #c4a463;
    --gold-light: #f7e9a8;
    --ink: #111111;
    --paper: #ffffff;
    --backdrop: #d9d9d9;
  }
  * { margin: 0; padding: 0; box-sizing: border-box; }
  html, body { width: 1200px; height: 1200px; overflow: hidden; background: var(--backdrop); }
  .canvas { position: relative; width: 1200px; height: 1200px; }
  .letterhead {
    position: absolute; left: 191px; top: 22px; width: 818px; height: 1158px;
    background: var(--paper); overflow: hidden;
    font-family: "Tinos", "Times New Roman", serif; color: var(--ink);
  }
  .header-band {
    position: absolute; left: 0; top: 0; width: 818px; height: 150px;
    background: linear-gradient(100deg, var(--navy) 0%, var(--navy) 45%, #8a7a55 75%, var(--gold-deep) 100%);
  }
  .brand-name {
    position: absolute; left: 87px; top: 194px; color: var(--navy);
    font-family: "Tinos", "Times New Roman", serif; font-weight: 700; line-height: 1;
  }
  .brand-name .primary { display: block; font-size: 43px; letter-spacing: -0.5px; }
  .brand-name .secondary { display: block; font-size: 23px; letter-spacing: 4.6px; margin-top: 6px; }
  .letter { position: absolute; left: 88px; top: 0; width: 660px; font-size: 17.2px; }
  .letter-date { position: absolute; right: 84px; top: 340px; font-size: 17.2px; }
  .line { position: absolute; left: 0; white-space: nowrap; }
  .footer-rule { position: absolute; left: 0; top: 1080px; width: 818px; height: 2px;
    background: linear-gradient(90deg, var(--gold-deep), var(--gold-light), var(--gold-deep)); }
  .footer-contact {
    position: absolute; left: 0; top: 1088px; width: 818px; text-align: center;
    font-family: "Cinzel", "Times New Roman", serif; font-weight: 500;
    font-size: 11.5px; letter-spacing: 0.6px; color: var(--navy); text-transform: uppercase;
    white-space: nowrap;
  }
  .footer-contact .email { font-size: 9.5px; }
</style>
</head>
<body>
<main class="canvas">
  <article class="letterhead">
    <div class="header-band" role="img" aria-label="Navy and gold decorative header sweep"></div>

    <div class="brand-name">
      <span class="primary">KESTREL BAY</span>
      <span class="secondary">STRATEGIES</span>
    </div>

    <p class="letter-date">December 21, 2025</p>

    <div class="letter">
      <p class="line" style="top:377px">Dear Sir,</p>
      <p class="line" style="top:450px">Thank you for inviting me to design your new letterhead.</p>
      <p class="line" style="top:523px">This letterhead is designed to embody simplicity, professionalism, and brand consistency.</p>
      <p class="line" style="top:560px">By using a clean layout with generous white space, the design ensures readability and</p>
      <p class="line" style="top:596px">a modern, uncluttered look. Your logo is placed prominently but tastefully, reinforcing brand</p>
      <p class="line" style="top:633px">recognition without overpowering the content. The color palette is based on navy blue and</p>
      <p class="line" style="top:669px">gold, maintaining a strong visual connection to the brand’s identity. Professional serif</p>
      <p class="line" style="top:706px">typography complements the contemporary style, ensuring that official correspondence looks</p>
      <p class="line" style="top:742px">polished and credible.</p>
      <p class="line" style="top:816px">Overall, the design balances corporate sophistication with the energetic, youthful spirit that</p>
      <p class="line" style="top:852px">defines you firm. I hope you like it.</p>
      <p class="line" style="top:925px">Best Regards,</p>
    </div>

    <div class="footer-rule"></div>
    <p class="footer-contact">218 Birch Avenue · Suite 310 · Juneau, Alaska 99801 · 555 014 2288 · <span class="email">info@kestrelbaystrategies.com</span></p>
  </article>
</main>
</body>
</html>
```